Stationery Design Project

KT7 Staffing requires letterhead and business card designs for a company based in London. Just like the name, we're a management resourcing company, providing resources to third party companies. You can see www.kt7staffing-example.com for ideas on existing colour schemes and design concepts that have been implimented and agreed to. Ultimately the design should broadcast professionalism, safety and the concept of growth.

Target Market(s)

Financial institutes; friendly societies (All UK based)

Industry/Entity Type

Safety

Requirements
Must have
• Files produced should be print ready; and the text in them editable (eg address, name etc)

```html
<!DOCTYPE html>
<html lang="en">
<head>
<meta charset="utf-8">
<title>KT7 Staffing – Stationery Design Project</title>
<link href="https://fonts.googleapis.com/css2?family=Arimo:wght@400;700&display=swap" rel="stylesheet">
<style>
  :root {
    --navy: #0a2a6b;
    --navy-deep: #061d52;
    --sky: #4fb6e6;
    --teal: #3aa6b9;
    --ink: #333333;
    --grey: #6b6b6b;
    --rule: #9a9a9a;
    --paper: #ffffff;
    --board: #ffffff;
    --photo-top: #2f4f8a;
    --photo-mid: #6b8fc7;
    --photo-low: #1a2d5c;
  }
  * { box-sizing: border-box; margin: 0; padding: 0; }
  html, body { width: 1200px; height: 900px; overflow: hidden; background: var(--board); }
  body { font-family: "Arimo", Arial, sans-serif; color: var(--ink); position: relative; }

  .brand { display: flex; align-items: center; gap: 8px; font-weight: 700; color: var(--teal); letter-spacing: .5px; white-space: nowrap; }
  .brand-mark { background: var(--teal); flex: none; }

  /* Letterhead */
  .letterhead { position: absolute; left: 33px; top: 45px; width: 590px; height: 762px; background: var(--paper); border: 1px solid #c9c9c9; overflow: hidden; }
  .letterhead-header { position: absolute; left: 0; top: 0; }
  .letterhead .brand { position: absolute; left: 26px; top: 40px; font-size: 30px; color: #7fd0ec; }
  .letterhead .brand-mark { width: 22px; height: 22px; background: #7fd0ec; }
  .header-contact { position: absolute; left: 384px; top: 22px; color: #fff; font-size: 10.5px; line-height: 17px; }
  .header-contact li { list-style: none; display: flex; align-items: center; gap: 9px; }
  .header-contact li:first-child { margin-bottom: 2px; }
  .header-contact svg { width: 10px; height: 10px; fill: #fff; flex: none; }
  .header-contact .spacer { width: 10px; }

  .letter-body { position: absolute; left: 109px; top: 176px; width: 414px; font-size: 9.6px; line-height: 12.6px; color: #444; }
  .letter-body h2 { font-size: 14px; font-weight: 700; color: #222; letter-spacing: .3px; margin-bottom: 22px; }
  .letter-body p { margin-bottom: 12px; }
  .letter-body section { margin-bottom: 24px; }
  .letter-body section.about { margin-bottom: 34px; }
  .sign-off { position: absolute; left: 109px; top: 630px; font-size: 9.6px; color: #444; }
  .signature-area { position: absolute; left: 109px; top: 645px; width: 120px; height: 52px; background: linear-gradient(90deg, #ececec, #f6f6f6); border-radius: 4px; }

  .letterhead-footer { position: absolute; left: 0; bottom: 0; width: 100%; height: 29px; background: var(--navy); color: #fff; font-size: 10.5px; letter-spacing: 2.4px; text-align: right; padding-right: 24px; line-height: 29px; }

  /* Business cards */
  .card { position: absolute; top: 45px; width: 251px; height: 198px; overflow: hidden; border-radius: 4px; background: var(--navy); }
  .card-front { left: 645px; }
  .card-back { left: 906px; }
  .card-photo { position: absolute; left: 0; top: 0; width: 100%; height: 120px; background: linear-gradient(180deg, var(--photo-top) 0%, var(--photo-mid) 45%, var(--photo-low) 100%); }
  .card-curve { position: absolute; left: 0; top: 70px; }
  .card-front .brand { position: absolute; left: 14px; top: 132px; font-size: 15px; color: #7fd0ec; gap: 5px; }
  .card-front .brand-mark { width: 11px; height: 11px; background: #7fd0ec; }
  .card-details { position: absolute; left: 138px; top: 127px; color: #fff; font-size: 5.4px; line-height: 7.4px; }
  .card-details .name { font-size: 9px; font-weight: 700; line-height: 10px; }
  .card-details .role { font-size: 5.6px; margin-bottom: 3px; }
  .card-details li { list-style: none; display: flex; align-items: center; gap: 4px; }
  .card-details svg { width: 5px; height: 5px; fill: #fff; flex: none; }
  .card-rule { position: absolute; left: 138px; right: 14px; top: 186px; height: 1px; background: #fff; opacity: .8; }
  .card-web { position: absolute; left: 138px; top: 189px; color: #fff; font-size: 5px; letter-spacing: 1.3px; }
  .card-back .card-photo { height: 100px; }
  .card-back .card-curve { top: 52px; }
  .card-back .brand { position: absolute; left: 44px; top: 140px; font-size: 22px; color: #7fd0ec; gap: 7px; }
  .card-back .brand-mark { width: 16px; height: 16px; background: #7fd0ec; }

  /* Project title */
  .project-brand { position: absolute; left: 830px; top: 752px; font-size: 30px; }
  .project-brand .brand-mark { width: 22px; height: 22px; }
  .project-rule { position: absolute; left: 832px; right: 0; top: 807px; height: 1px; background: var(--rule); }
  .project-title { position: absolute; left: 834px; top: 811px; font-size: 26px; color: var(--grey); font-weight: 400; }
</style>
</head>
<body>

<article class="letterhead">
  <svg class="letterhead-header" width="590" height="170" viewBox="0 0 590 170" aria-hidden="true">
    <path d="M0 0H590V104C420 110 200 128 0 150Z" fill="var(--navy)"/>
    <path d="M0 150C200 128 420 110 590 104V110C420 116 220 138 0 162Z" fill="var(--sky)"/>
  </svg>
  <div class="brand"><span class="brand-mark"></span>KT7 Staffing</div>
  <ul class="header-contact">
    <li><span class="spacer"></span>27 Harrow Lane, City of London</li>
    <li><svg viewBox="0 0 10 10"><path d="M2 0.5 3.6 2.6 2.7 3.7C3.3 5 4.8 6.6 6.3 7.3L7.4 6.4 9.5 8 8.4 9.5C4.5 9.3 0.7 5.5 0.5 1.6Z"/></svg>020 7946 0381</li>
    <li><svg viewBox="0 0 10 10"><path d="M3 0H7A.8.8 0 0 1 7.8.8V9.2A.8.8 0 0 1 7 10H3A.8.8 0 0 1 2.2 9.2V.8A.8.8 0 0 1 3 0ZM3 1.2V8H7V1.2Z"/></svg>020 7946 0381</li>
    <li><svg viewBox="0 0 10 10"><path d="M0 2H10V8H0ZM.8 2.6 5 5.6 9.2 2.6V3.4L5 6.4.8 3.4Z"/></svg>office@kt7staffing-example.com</li>
  </ul>

  <div class="letter-body">
    <section class="about">
      <h2>ABOUT US</h2>
      <p>Through a dedicated team of professionals, with at least fifteen years of experience in their various fields, we offer our clients a focused service of problem solving, key consultation and driving change for all of the challenges of modern business. Our unique approach means that our team of professionals work from the inside. They see the problems from the ground floor and are able to offer tailored advice on a range of business issues.</p>
    </section>
    <section>
      <h2>OUR CULTURE</h2>
      <p>KT7 Staffing is a multi-national company with clients in North America, Europe and Africa. We hire only seasoned professionals with at least 10 - 15 years of experience in their relevant fields. All of whom exemplify our core business values – Professionalism, Talent, Integrity and Loyalty.</p>
      <p>Our professionals are guided by the innovative culture at KT7 Staffing, a culture which puts great emphasis on teamwork, results and flexibility. When our team of professionals go inside any business they do so with an open mind, ready to address any multitude of issues that may present themselves. Our custom approach is unique to each of our clients, ensuring the each client receives the best service possible.</p>
      <p>Our work is results oriented. Because when our clients succeed, so do we.</p>
    </section>
    <section>
      <h2>OUR LEADERSHIP</h2>
      <p>Our leadership team possess a rich and diverse industry knowledge, delivering an unprecedented level of commitment and value to our customers.</p>
      <p>We are currently updating our leadership team's profiles, please check back again soon.</p>
    </section>
  </div>
  <p class="sign-off">Director</p>
  <div class="signature-area" role="img" aria-label="Handwritten signature of the director"></div>

  <footer class="letterhead-footer">www.kt7staffing-example.com</footer>
</article>

<div class="card card-front">
  <div class="card-photo" role="img" aria-label="Photograph of City of London office towers against a blue sky"></div>
  <svg class="card-curve" width="251" height="80" viewBox="0 0 251 80" aria-hidden="true">
    <path d="M0 48C90 34 170 24 251 20V80H0Z" fill="var(--navy)"/>
  </svg>
  <div class="brand"><span class="brand-mark"></span>KT7 Staffing</div>
  <div class="card-details">
    <p class="name">Your Name</p>
    <p class="role">Current Position</p>
    <ul>
      <li>27 Harrow Lane, City of London</li>
      <li><svg viewBox="0 0 10 10"><path d="M2 0.5 3.6 2.6 2.7 3.7C3.3 5 4.8 6.6 6.3 7.3L7.4 6.4 9.5 8 8.4 9.5C4.5 9.3 0.7 5.5 0.5 1.6Z"/></svg>020 7946 0381</li>
      <li><svg viewBox="0 0 10 10"><path d="M3 0H7A.8.8 0 0 1 7.8.8V9.2A.8.8 0 0 1 7 10H3A.8.8 0 0 1 2.2 9.2V.8A.8.8 0 0 1 3 0ZM3 1.2V8H7V1.2Z"/></svg>020 7946 0381</li>
      <li><svg viewBox="0 0 10 10"><path d="M0 2H10V8H0ZM.8 2.6 5 5.6 9.2 2.6V3.4L5 6.4.8 3.4Z"/></svg>office@kt7staffing-example.com</li>
    </ul>
  </div>
  <div class="card-rule"></div>
  <p class="card-web">www.kt7staffing-example.com</p>
</div>

<div class="card card-back">
  <div class="card-photo" role="img" aria-label="Photograph of City of London office towers against a blue sky"></div>
  <svg class="card-curve" width="251" height="146" viewBox="0 0 251 146" aria-hidden="true">
    <path d="M0 56C90 42 170 30 251 26V146H0Z" fill="var(--navy)"/>
  </svg>
  <div class="brand"><span class="brand-mark"></span>KT7 Staffing</div>
</div>

<div class="brand project-brand"><span class="brand-mark"></span>KT7 Staffing</div>
<div class="project-rule"></div>
<h1 class="project-title">Stationery Design Project</h1>

</body>
</html>
```